Outdoor sign for Brindle Auto Restoration

I need a horizontal 4'x 8' outdoor roadside sign for my classic auto restoration business. I have uploaded colors and our logo. Needs the Brindle name, a prominent Classic AUTO RESTORATION, phone number and website. We rebuild and restore vintage cars, trucks and 4x4s. I'd like something clean but possibly retro. Classic Auto Restoration is more important than the Brindle name. It needs to be visible and readable from the street. NO CLIP ART

Target Market(s)

Customers who need their vintage care restored or upgraded. Men and women ages 25-75

Industry/Entity Type

Automotive

Colors
FFC000
F8CF3A
FAE287
FDF2CF
FEFAEE

Requirements
Must have
• Legible. Bright. Readable as a backlit 4' x 8' large horizontal sign (roughly 120cm X 240cm)
Nice to have
• Use of the Brindle logo/type, Complete or Classic before prominent AUTO RESTORATION
Should not have
• Clip art of old cars or icons. And we don't want the Brindle Logo from the website because it wont be legible from the road. I have included the Illustrator file for Brindle text in the uploads

```html
<!DOCTYPE html>
<html lang="en">
<head>
<meta charset="utf-8">
<title>Brindle Auto Restoration Sign</title>
<link href="https://fonts.googleapis.com/css2?family=Bebas+Neue&family=Oswald:wght@700&family=Roboto+Condensed:wght@700&display=swap" rel="stylesheet">
<style>
  :root {
    --sign-dark: #2b2725;
    --brand-gold: #f2ae00;
    --text-white: #ffffff;
    --photo-yellow: #d99a10;
    --photo-red: #8e1420;
    --photo-grey: #3a3838;
  }
  html, body {
    margin: 0;
    padding: 0;
    width: 1200px;
    height: 600px;
    overflow: hidden;
    background: var(--sign-dark);
  }
  .sign {
    position: relative;
    width: 1200px;
    height: 600px;
    background: var(--sign-dark);
    overflow: hidden;
  }
  .sign__photo {
    position: absolute;
    left: 0;
    top: 0;
    width: 830px;
    height: 600px;
    background:
      linear-gradient(90deg, rgba(43,39,37,0) 60%, var(--sign-dark) 100%),
      linear-gradient(100deg, var(--photo-yellow) 0%, var(--photo-yellow) 30%, var(--photo-red) 40%, var(--photo-red) 52%, var(--photo-grey) 68%, var(--sign-dark) 100%);
  }
  .headline {
    position: absolute;
    left: 602px;
    top: 40px;
    margin: 0;
    font-family: "Bebas Neue", sans-serif;
    font-weight: 400;
    color: var(--brand-gold);
    font-size: 124px;
    line-height: 0.92;
    letter-spacing: 2px;
  }
  .headline__line { display: block; white-space: nowrap; }
  .headline__line--second { letter-spacing: 4.5px; }
  .brand-name {
    position: absolute;
    left: 614px;
    top: 386px;
    margin: 0;
    font-family: "Oswald", sans-serif;
    font-weight: 700;
    color: var(--brand-gold);
    font-size: 114px;
    line-height: 1;
    letter-spacing: 2px;
    text-transform: uppercase;
  }
  .contact {
    position: absolute;
    left: 614px;
    top: 520px;
    display: flex;
    align-items: center;
    gap: 24px;
    font-family: "Roboto Condensed", sans-serif;
    font-weight: 700;
    font-size: 33px;
    color: var(--text-white);
    white-space: nowrap;
  }
  .contact__dot {
    width: 10px;
    height: 10px;
    border-radius: 50%;
    background: var(--brand-gold);
  }
</style>
</head>
<body>
  <main class="sign">
    <div class="sign__photo" role="img" aria-label="Row of polished vintage cars in yellow, red and dark grey, seen from the front with chrome headlights and grilles"></div>
    <h1 class="headline">
      <span class="headline__line">Classic Auto</span>
      <span class="headline__line headline__line--second">Restoration</span>
    </h1>
    <p class="brand-name">Brindle</p>
    <div class="contact">
      <span class="contact__phone">501-555-0147</span>
      <span class="contact__dot"></span>
      <span class="contact__web">brindle autoworks.com</span>
    </div>
  </main>
</body>
</html>
```